Venthrax - Joint website

Recently, three of our organizations: Norvelle, PRISM, and Talomir have united to work on a single project - Advanced Recycling of plastic waste via technology - Venthrax. For this united project, we need a new design of the website under the name of Venthrax which would feature the three companies.

Target Market(s)

Suppliers, consumers, and consumer brand companies within the Petrochemicals industry

Coding

Coded - Design and coding required

Number of Pages Required

1 page

Font styles to use
Other font styles liked:
• Lato

Requirements
Must have
• A clear image of how the Venthrax technology works/Sustainable aspect elaborated. The video on the home page featuring the three company representatives: https://www.examplevideo-host.com/watch?v=qTZP7LMWDA4&ab_channel=brightworkHelper
Nice to have
• Make use of icons, explained with some text for the technology. / make clear which role every company has within this initiative. / Picture of the first truck, with the banner of the three companies. / short video of the factory and technology.
Should not have
• A divided theme, it must be clear that it is a collaborated initiative, and that we all work together within our own expertise. / No cliché sustainability pictures, that aren’t relevant to the product.

```html
<!DOCTYPE html>
<html lang="en">
<head>
<meta charset="utf-8">
<title>Venthrax – Advanced Recycling</title>
<link href="https://fonts.googleapis.com/css2?family=Lato:wght@400;700&family=Roboto:wght@500;700;900&display=swap" rel="stylesheet">
<style>
:root{
  --green:#1e8a4c;
  --green-dark:#136b38;
  --orange:#c65a2a;
  --ink:#1b1b1b;
  --text:#555;
  --line:#e3e3e3;
  --footer:#111;
  --white:#fff;
}
*{box-sizing:border-box;margin:0;padding:0}
html,body{width:1200px;height:5025px;overflow:hidden}
body{font-family:'Lato',sans-serif;color:var(--text);background:var(--white);position:relative}
.head{font-family:'Roboto',sans-serif;font-weight:700;color:var(--ink);text-transform:uppercase;text-align:center;font-size:36px}
.abs{position:absolute}

/* nav */
.nav{position:absolute;top:0;left:0;width:1200px;height:64px;display:flex;align-items:center}
.brand{position:absolute;left:111px;font-family:'Lato',sans-serif;font-weight:700;font-size:34px;color:#444;letter-spacing:1px}
.menu{position:absolute;right:111px;display:flex;gap:46px;font-family:'Roboto',sans-serif;font-weight:500;font-size:15px;color:var(--ink);text-transform:uppercase}

/* hero */
.hero{position:absolute;top:64px;left:0;width:1200px;height:619px;background:linear-gradient(180deg,#8e8a82 0%,#d9b27a 22%,#a99a86 38%,#7f8a7e 60%,#5c6a60 100%)}
.hero-box{position:absolute;left:94px;top:166px;width:466px;height:287px;background:rgba(40,40,40,.55);padding:26px 16px}
.hero-box h1{font-family:'Roboto',sans-serif;font-weight:700;font-size:37px;line-height:46px;color:var(--white);text-transform:uppercase}
.hero-box p{color:var(--white);font-size:15px;line-height:27px;margin-top:12px}
.btn-green{display:inline-block;background:var(--green);color:var(--white);font-family:'Roboto',sans-serif;font-weight:700;font-size:15px;border-radius:30px;padding:17px 37px;text-transform:uppercase}
.hero-box .btn-green{margin-top:24px}
.hero-arrow{position:absolute;top:290px}
.dots{position:absolute;top:568px;left:565px;display:flex;gap:10px}
.dots span{width:10px;height:10px;border-radius:50%;background:rgba(255,255,255,.5)}
.dots span:first-child{background:var(--white)}

/* challenges */
.challenges .head{position:absolute;top:756px;width:1200px}
.ch-card{position:absolute;top:825px;width:316px;height:338px;border:1px solid var(--line);text-align:center;padding:32px 14px}
.ch-card .ic{width:114px;height:114px;border-radius:50%;background:var(--green);margin:0 auto 34px;display:flex;align-items:center;justify-content:center}
.ch-card p{font-size:15px;line-height:27px}

/* solution */
.sol-img{position:absolute;top:1249px;left:0;width:600px;height:493px;background:linear-gradient(160deg,#8b8f86,#b9b3a3 45%,#6d7a6c)}
.sol{position:absolute;top:1249px;left:600px;width:600px;height:493px;background:var(--orange);padding:80px 115px 0 69px;color:var(--white)}
.sol h2{font-family:'Roboto',sans-serif;font-weight:700;font-size:37px;text-transform:uppercase}
.sol p{font-size:14px;line-height:29px;margin-top:14px;text-align:justify}
.sol p+p{margin-top:10px}
.btn-outline{display:inline-block;border:2px solid var(--white);border-radius:30px;padding:16px 44px;font-family:'Roboto',sans-serif;font-weight:700;font-size:15px;margin-top:34px;text-transform:uppercase;color:var(--white)}

/* video */
.video{position:absolute;top:1742px;left:0;width:1200px;height:515px;background:radial-gradient(ellipse at 60% 45%,#5a5046 0%,#2e2a25 45%,#151311 100%)}
.play{position:absolute;left:553px;top:185px;width:94px;height:94px;border-radius:50%;background:var(--white);border:6px solid #cfcfcf;display:flex;align-items:center;justify-content:center}

/* how */
.how .head{position:absolute;top:2333px;width:1200px}
.step{position:absolute;top:2472px;width:210px;text-align:center}
.step .ic{width:76px;height:76px;border-radius:50%;background:var(--green);margin:0 auto 14px;display:flex;align-items:center;justify-content:center}
.step p{font-size:14px;line-height:26px;color:#444}

/* products */
.products{position:absolute;top:2708px;left:0;width:1200px;height:624px;background:linear-gradient(180deg,rgba(30,138,76,.95),rgba(19,107,56,.92)),linear-gradient(90deg,#2d5b3b,#4f7c58)}
.products .head{position:absolute;top:74px;width:1200px;color:var(--white)}
.pr-card{position:absolute;top:146px;width:312px;height:400px;background:var(--white);text-align:center;padding:20px 26px}
.pr-img{width:70px;height:160px;margin:0 auto;border-radius:10px;background:linear-gradient(90deg,#d9d9d9,#fafafa,#cfcfcf)}
.pr-card h3{font-family:'Roboto',sans-serif;font-weight:700;font-size:20px;color:var(--ink);margin-top:18px}
.pr-card p{font-size:14px;line-height:26px;margin-top:10px}
.btn-orange{display:inline-block;background:var(--orange);color:var(--white);font-family:'Roboto',sans-serif;font-weight:700;font-size:15px;border-radius:30px;padding:15px 34px;margin-top:16px;text-transform:uppercase}

/* technology */
.tech-intro{position:absolute;left:139px;top:3456px;width:280px}
.tech-intro h2{font-family:'Roboto',sans-serif;font-weight:700;font-size:37px;line-height:50px;color:var(--ink);text-transform:uppercase}
.tech-intro p{font-weight:700;font-size:13px;line-height:24px;color:#444;margin-top:14px}
.more{display:inline-block;font-family:'Roboto',sans-serif;font-weight:700;font-size:13px;color:var(--orange);text-transform:uppercase;margin-top:20px}
.tc{position:absolute;width:310px;height:320px;background:var(--white);box-shadow:0 0 14px rgba(0,0,0,.08);padding:40px 18px 0}
.tc .num{position:absolute;right:26px;top:24px;font-family:'Roboto',sans-serif;font-weight:900;font-size:104px;line-height:1;color:#f2f2f2}
.tc .ic{position:relative;width:50px;height:50px}
.tc h3{position:relative;font-family:'Roboto',sans-serif;font-weight:500;font-size:21px;color:var(--ink);margin-top:18px}
.tc p{font-size:14px;line-height:25px;margin-top:12px}
.tc .more{margin-top:22px}

/* partners */
.partners{position:absolute;top:4152px;left:0;width:1200px;height:546px;background:linear-gradient(180deg,#f5f6f5,#e9ebe9 60%,#f3f3f3)}
.partners .head{position:absolute;top:58px;width:1200px}
.pa-card{position:absolute;top:127px;width:316px;height:331px;background:var(--white);border:1px solid var(--line);padding:0 20px}
.pa-logo{height:112px;display:flex;align-items:center;justify-content:center;gap:10px;font-family:'Lato',sans-serif;font-weight:700;font-size:40px;color:var(--ink)}
.pa-card p{font-size:15px;line-height:27px}

/* footer */
.footer{position:absolute;top:4698px;left:0;width:1200px;height:327px;background:var(--footer);color:var(--white)}
.f-brand{position:absolute;left:111px;top:80px;font-weight:700;font-size:42px}
.social{position:absolute;left:117px;top:150px;display:flex;gap:8px}
.social span{width:30px;height:30px;border-radius:50%;background:var(--white)}
.f-col{position:absolute;top:92px}
.f-col h4{font-family:'Roboto',sans-serif;font-weight:500;font-size:20px;margin-bottom:14px}
.f-col li{list-style:none;font-size:13px;line-height:28px}
.f-col li svg{vertical-align:-2px;margin-right:8px}
.email{width:254px;height:40px;border:1px solid var(--white);border-radius:22px;padding:0 18px;display:flex;align-items:center;font-size:13px}
.f-col .btn-green{padding:12px 26px;font-size:14px;margin-top:16px}
.f-rule{position:absolute;left:111px;top:257px;width:976px;height:1px;background:#333}
.copy{position:absolute;top:287px;width:1200px;text-align:center;font-size:12px}
</style>
</head>
<body>

<header class="nav">
  <div class="brand">venthrax</div>
  <nav class="menu"><span>Home</span><span>Meet the partners</span><span>Technology</span><span>System &amp; Operations</span><span>Contact</span></nav>
</header>

<section class="hero" role="img" aria-label="Photograph of a large heap of mixed plastic waste under a sunset sky">
  <div class="hero-box">
    <h1>Converting waste to circular resource!</h1>
    <p>Lorem ipsum dolor sit amet, consectetur adipiscing elit, sed do eiusmod tempor incididunt</p>
    <span class="btn-green">Get started</span>
  </div>
  <svg class="hero-arrow" style="left:70px" width="16" height="30"><path d="M14 2 2 15l12 13" fill="none" stroke="#fff" stroke-width="2"/></svg>
  <svg class="hero-arrow" style="right:70px" width="16" height="30"><path d="M2 2l12 13L2 28" fill="none" stroke="#fff" stroke-width="2"/></svg>
  <div class="dots"><span></span><span></span><span></span><span></span></div>
</section>

<section class="challenges">
  <h2 class="head">Current challenges</h2>
  <div class="ch-card" style="left:111px">
    <div class="ic"><svg width="60" height="60" fill="none" stroke="#fff" stroke-width="3"><circle cx="30" cy="30" r="7"/><circle cx="10" cy="10" r="4"/><circle cx="50" cy="10" r="4"/><circle cx="10" cy="50" r="4"/><circle cx="50" cy="50" r="4"/><path d="M13 13l12 12M47 13 35 25M13 47l12-12M47 47 35 35"/></svg></div>
    <p>Today polymers are the dominating materials for most application in modern life. Global demand for polymers will double within the next 30 years</p>
  </div>
  <div class="ch-card" style="left:441px">
    <div class="ic"><svg width="60" height="60" fill="none" stroke="#fff" stroke-width="3"><path d="M30 8 18 28h10M30 8l12 20M42 28l-8 0M10 40l10 14h20l10-14M36 28l6 10"/><path d="M25 22l5-8 5 8"/></svg></div>
    <p>Compounds, additives, colorants and contaminants put the limits to the recycling of polymers. More than 50% of all polymer waste is rejected and incinerated</p>
  </div>
  <div class="ch-card" style="left:771px">
    <div class="ic"><svg width="60" height="60" fill="none" stroke="#fff" stroke-width="3"><path d="M6 54h48M10 54V30l10 6v-6l10 6v-6l10 6V14h8v40"/><path d="M18 46h4M28 46h4M38 46h4"/></svg></div>
    <p>Our industry is failing to meet the sustainability goals set by the EU.</p>
  </div>
</section>

<div class="sol-img" role="img" aria-label="Photograph of a worker with a tablet in front of stacked bales of compressed plastic"></div>
<section class="sol">
  <h2>Our solution!</h2>
  <p>Advanced Recycling via Venthrax Technology!</p>
  <p>VENTHRAX's advanced depolymerisation technology allows the regeneration of a high quality liquid resource suitable for the production of new virgin quality polymers. It is applicable to mixed and contaminated plastics and of high efficiency.</p>
  <span class="btn-outline">Contact us</span>
</section>

<section class="video" role="img" aria-label="Video still of a partner representative speaking about the joint Venthrax recycling initiative, with a play button">
  <div class="play"><svg width="26" height="28"><path d="M4 2l20 12L4 26z" fill="var(--orange)"/></svg></div>
</section>

<section class="how">
  <h2 class="head">How does it work?</h2>
  <svg class="abs" style="left:0;top:2400px" width="1200" height="150">
    <g fill="none" stroke="var(--green)" stroke-width="5">
      <path d="M132 20q-28-10-42 12"/><path d="M88 80q6 26 40 20"/>
      <path d="M1068 20q28-10 42 12"/><path d="M1080 106q30 4 40-16"/>
      <path d="M328 25h-30M523 25h-30M717 25h-30M910 25h-30"/>
      <path d="M358 111h32M600 111h32M864 111h32"/>
    </g>
    <g fill="var(--green)">
      <path d="M136 12l10 10-14 6z"/><path d="M92 72l-10 14 14 2z"/>
      <path d="M1064 12l-10 10 14 6z"/><path d="M1116 82l12 6-10 10z"/>
      <path d="M288 25l14-10v20zM483 25l14-10v20zM677 25l14-10v20zM870 25l14-10v20z"/>
      <path d="M400 111l-14-10v20zM642 111l-14-10v20zM906 111l-14-10v20z"/>
    </g>
  </svg>
  <div class="step" style="left:143px"><div class="ic"><svg width="34" height="40" fill="none" stroke="#fff" stroke-width="3"><path d="M12 3h10v6l4 5v23H8V14l4-5z"/><path d="M8 22h18"/></svg></div><p>A plastic product is produced and used by individua customers</p></div>
  <div class="step" style="left:395px"><div class="ic"><svg width="34" height="40" fill="none" stroke="#fff" stroke-width="3"><path d="M4 8h26M12 8V4h10v4M7 8l2 29h16l2-29M14 14v18M20 14v18"/></svg></div><p>After being used, the product is being disposed off</p></div>
  <div class="step" style="left:648px"><div class="ic"><svg width="40" height="40" fill="none" stroke="#fff" stroke-width="3"><path d="M20 4l-8 14h8M20 4l8 14M6 26l6 10h16l6-10"/></svg></div><p>The waste is collected and processed via Venthrax's advanced recycling technology</p></div>
  <div class="step" style="left:904px"><div class="ic"><svg width="40" height="40" fill="none" stroke="#fff" stroke-width="3"><path d="M4 36h32M7 36V20l8 5v-5l8 5V10h8v26"/></svg></div><p>The recycled oils are handled by the plastic product producer</p></div>
</section>

<section class="products" role="img" aria-label="Green-tinted photograph of collected plastic waste behind the product cards">
  <h2 class="head">Our products</h2>
  <div class="pr-card" style="left:111px"><div class="pr-img" role="img" aria-label="White plastic bottle"></div><h3>Product Name</h3><p>Lorem ipsum dolor sit amet, consectetur adipiscing elit, sed do eiusmod tempor incididunt ut labore et dolore</p><span class="btn-orange">Learn more</span></div>
  <div class="pr-card" style="left:443px"><div class="pr-img" role="img" aria-label="White spray bottle"></div><h3>Product Name</h3><p>Lorem ipsum dolor sit amet, consectetur adipiscing elit, sed do eiusmod tempor incididunt ut labore et dolore</p><span class="btn-orange">Learn more</span></div>
  <div class="pr-card" style="left:776px"><div class="pr-img" role="img" aria-label="Clear water bottle" style="background:linear-gradient(90deg,#9cc7e6,#e6f3fb,#8dbfe0)"></div><h3>Product Name</h3><p>Lorem ipsum dolor sit amet, consectetur adipiscing elit, sed do eiusmod tempor incididunt ut labore et dolore</p><span class="btn-orange">Learn more</span></div>
</section>

<section class="technology">
  <div class="tech-intro">
    <h2>Our technology</h2>
    <p>Lorem ipsum dolor smet, consectetur adipiscig eit, se od tempor</p>
    <span class="more">Read more →</span>
  </div>
  <div class="tc" style="left:443px;top:3398px"><span class="num">01</span><svg class="ic" fill="none" stroke="var(--green)" stroke-width="2"><rect x="6" y="4" width="34" height="26"/><path d="M10 10h26M10 16h16"/><circle cx="32" cy="36" r="9"/></svg><h3>The standard Lorem</h3><p>Lorem ipsum dolor smet, consectetur adipiscig eit, se od tempor incididunt ut labore et dole magna aliqua. Quis ipsum suspendisse</p><span class="more">Read more →</span></div>
  <div class="tc" style="left:777px;top:3398px"><span class="num">02</span><svg class="ic" fill="none" stroke="var(--green)" stroke-width="2"><rect x="8" y="8" width="28" height="34"/><path d="M14 16h16M14 24h16M14 32h10"/><circle cx="38" cy="10" r="6"/></svg><h3>The standard Lorem</h3><p>Lorem ipsum dolor smet, consectetur adipiscig eit, se od tempor incididunt ut labore et dole magna aliqua. Quis ipsum suspendisse</p><span class="more">Read more →</span></div>
  <div class="tc" style="left:111px;top:3742px"><span class="num">03</span><svg class="ic" fill="none" stroke="var(--green)" stroke-width="2"><rect x="4" y="6" width="40" height="28"/><path d="M10 14h14M10 20h20M10 26h8"/><circle cx="36" cy="38" r="8"/></svg><h3>The standard Lorem</h3><p>Lorem ipsum dolor smet, consectetur adipiscig eit, se od tempor incididunt ut labore et dole magna aliqua. Quis ipsum suspendisse</p><span class="more">Read more →</span></div>
  <div class="tc" style="left:443px;top:3742px"><span class="num">04</span><svg class="ic" fill="none" stroke="var(--green)" stroke-width="2"><circle cx="24" cy="20" r="14"/><circle cx="24" cy="20" r="6"/><path d="M16 34v12h16V34"/></svg><h3>The standard Lorem</h3><p>Lorem ipsum dolor smet, consectetur adipiscig eit, se od tempor incididunt ut labore et dole magna aliqua. Quis ipsum suspendisse</p><span class="more">Read more →</span></div>
  <div class="tc" style="left:777px;top:3742px"><span class="num">05</span><svg class="ic" fill="none" stroke="var(--green)" stroke-width="2"><circle cx="18" cy="18" r="10"/><circle cx="32" cy="30" r="10"/><path d="M18 40v8M14 44h8"/></svg><h3>The standard Lorem</h3><p>Lorem ipsum dolor smet, consectetur adipiscig eit, se od tempor incididunt ut labore et dole magna aliqua. Quis ipsum suspendisse</p><span class="more">Read more →</span></div>
</section>

<section class="partners">
  <h2 class="head">Partners in Venthrax</h2>
  <div class="pa-card" style="left:111px"><div class="pa-logo">PRISM</div><p>PRISM represents a diverse group of companies contributing to a sustainable future. We handle, trade, and explore commodities in energy, and renewables markets, with the aim to bring sustainability into a predominantly unsustainable market.</p></div>
  <div class="pa-card" style="left:441px"><div class="pa-logo" style="color:var(--green)">NORVELLE</div><p>NORVELLE specializes in lid films, rigid/flexible films and bags. Films are printed using flexographic, gravure and digital printing processes. Their aspiration is to find the optimal packaging solution for all kinds of products.</p></div>
  <div class="pa-card" style="left:771px"><div class="pa-logo" style="color:#1f5e9e">TALOMIR</div><p>TALOMIR GmbH is with its engineers and technicians specialists in industrial plant engineering. Founded as a spin-off from a traditional German plant manufacturer, we develop and implement solutions for the growing demand for secondary raw materials.</p></div>
</section>

<footer class="footer">
  <div class="f-brand">venthrax</div>
  <div class="social"><span></span><span></span></div>
  <div class="f-col" style="left:363px"><h4>Links</h4><ul><li>Home</li><li>Meet the partners</li><li>Technology</li><li>System &amp; Operations</li><li>Contact</li></ul></div>
  <div class="f-col" style="left:546px"><h4>Contact Us</h4><ul>
    <li><svg width="11" height="11"><path d="M2 1l3 0 1 3-2 1q1 3 4 4l1-2 3 1v3q-9 0-10-10z" fill="#fff"/></svg>888 888 8888</li>
    <li><svg width="12" height="10"><rect x="0.5" y="0.5" width="11" height="9" fill="none" stroke="#fff"/><path d="M1 1l5 4 5-4" fill="none" stroke="#fff"/></svg>info@venthrax.com</li>
    <li><svg width="10" height="13"><path d="M5 12S1 7 1 5a4 4 0 0 1 8 0c0 2-4 7-4 7z" fill="#fff"/></svg>123 Avenue name, City name</li>
    <li style="padding-left:18px">10150, United States</li></ul></div>
  <div class="f-col" style="left:835px"><h4>Sign Up for Newsletter</h4><div class="email">Email</div><span class="btn-green">Sign up now</span></div>
  <div class="f-rule"></div>
  <div class="copy">© 2021 Venthrax . All Rights Reserved.</div>
</footer>

</body>
</html>
```